Mar-wick Sky Harbor Custom Brokers Limited

The Company deals with:
shipping
logistic
imports
Export
customs clearance (customs broker services); and
customers can shop online and we take care of the shipment from the United States of America to Jamaica.
(we offer freight forwarding services from USA to Kingston Jamaica
Our tagline is : Creating Waves in the Logistic Industry.
Address: Shop 9 Birchfield Trade Centre, 227-229 Welland Avenue Kingston 8, Jamaica West Indies Telephone: (876)555-0193
Example of what we required can be seem: www.swiftparcelhubexample.com

```html
<!DOCTYPE html>
<html lang="en">
<head>
<meta charset="utf-8">
<title>Mar-wick Sky Harbor Custom Brokers Limited</title>
<link href="https://fonts.googleapis.com/css2?family=Roboto:wght@400;500;700;900&display=swap" rel="stylesheet">
<style>
:root{
  --navy:#0d2b52;
  --navy-deep:#0a2141;
  --gold:#eba800;
  --gold-soft:#f4b400;
  --ink:#1b1b1b;
  --grey:#6d6d6d;
  --line:#e3e3e3;
  --white:#fff;
}
*{box-sizing:border-box;margin:0;padding:0}
html,body{width:1200px;height:3923px;overflow:hidden}
body{font-family:"Roboto",Arial,sans-serif;color:var(--ink);background:var(--white);position:relative}
a{color:inherit;text-decoration:none}
.abs{position:absolute}

/* top bar */
.topbar{position:absolute;top:0;left:0;width:1200px;height:26px;background:var(--navy);color:#fff;font-size:13px;font-weight:500}
.topbar .welcome{position:absolute;left:63px;top:6px}
.topbar .login{position:absolute;left:922px;top:6px}
.topbar .social{position:absolute;left:1054px;top:6px;display:flex;gap:5px}
.topbar .social span{width:14px;height:14px;background:#fff;border-radius:2px}

/* nav */
.nav{position:absolute;top:26px;left:0;width:1200px;height:93px;background:#fff;font-size:15px;font-weight:500}
.nav a{position:absolute;top:38px}
.nav a.active{color:var(--gold)}
.brand{position:absolute;left:505px;top:16px;width:190px;text-align:center}
.brand .mark{width:28px;height:28px;border-radius:50%;background:var(--gold);margin:0 auto 6px}
.brand .name{font-size:14px;font-weight:700;color:var(--navy);letter-spacing:.5px}
.brand .sub{font-size:8px;color:var(--navy);letter-spacing:3px;margin-top:3px}

/* hero */
.hero{position:absolute;top:119px;left:0;width:1200px;height:483px;background:radial-gradient(ellipse at 50% 45%,#1d5166 0%,#123a4e 45%,#0b2636 100%)}
.hero-brand{position:absolute;left:0;width:1200px;top:220px;text-align:center;color:#fff}
.hero-brand .name{font-size:30px;font-weight:700;letter-spacing:1.5px}
.hero-brand .sub{font-size:15px;letter-spacing:8px;margin-top:8px}
.btn{display:inline-block;background:var(--gold);color:#fff;font-weight:700;text-transform:uppercase;text-align:center}
.hero .btn{position:absolute;left:491px;top:300px;width:218px;height:37px;line-height:33px;font-size:17px;border:2px solid #fff;outline:2px solid var(--gold)}
.dots{position:absolute;top:414px;left:563px;display:flex;gap:14px}
.dots span{width:11px;height:11px;border-radius:50%;background:#fff}
.dots span.on{background:var(--gold)}

/* strip */
.strip{position:absolute;top:602px;left:87px;width:1026px;height:239px;display:flex}
.strip .panel{width:342px;height:239px}
.strip .p1{background:linear-gradient(135deg,#c9b08c,#8e7a62 60%,#5a5d66)}
.strip .p3{background:linear-gradient(135deg,#d6a55a,#b78540 55%,#8a6a48)}
.strip .p2{position:relative;background:linear-gradient(135deg,#4b6b9e,#2a4a86);border:6px solid var(--gold);color:#fff;text-align:center;padding:36px 24px 0}
.strip .p2 h3{color:var(--gold);font-size:17px;font-weight:500;text-transform:uppercase;margin-bottom:4px}
.strip .p2 p{font-size:13px;line-height:20px}
.strip .p2 .btn{margin-top:18px;width:152px;height:40px;line-height:40px;font-size:15px}
.arrow-l,.arrow-r{position:absolute;top:109px;width:24px;height:24px;background:var(--gold);color:#fff;font-size:16px;font-weight:700;text-align:center;line-height:24px}
.arrow-l{left:2px}.arrow-r{right:2px}

/* why */
.why-photo{position:absolute;left:139px;top:929px;width:525px;height:350px;border:7px solid var(--gold);background:linear-gradient(160deg,#cfd8e2,#3e5fa8 45%,#7b8ea0)}
.why-text{position:absolute;left:689px;top:929px;width:380px}
.why-text h2{font-size:30px;font-weight:700;color:var(--navy);margin-bottom:18px}
.why-text p{font-size:13px;line-height:23px;color:var(--grey);margin-bottom:23px}
.read-more{color:var(--gold);font-weight:500;font-size:16px}
.why-icons{position:absolute;top:1204px;left:689px;display:flex;gap:31px}
.why-icons span{width:66px;height:66px;border-radius:50%;background:var(--gold);display:flex;align-items:center;justify-content:center}

/* features band */
.features{position:absolute;top:1368px;left:0;width:1200px;height:269px;background:var(--navy)}
.feature{position:absolute;top:32px;width:176px;text-align:center;color:#fff}
.feature .ring{width:176px;height:176px;border-radius:50%;border:4px solid var(--gold);display:flex;align-items:center;justify-content:center}
.feature h4{font-size:19px;font-weight:700;margin-top:12px}

/* blog */
.sec-title{position:absolute;left:0;width:1200px;text-align:center;font-size:30px;font-weight:700}
.post{position:absolute;top:1768px;width:330px;height:425px;background:#fff;box-shadow:0 1px 6px rgba(0,0,0,.18)}
.post .ph{height:177px}
.post .body{padding:14px 16px}
.post h3{font-size:21px;line-height:28px;font-weight:500;color:var(--ink)}
.post.featured h3{color:var(--gold)}
.post .meta{font-size:13px;color:#444;margin:10px 0 18px;display:flex;gap:14px}
.post p{font-size:13px;line-height:21px;color:var(--grey)}
.post .more{display:block;margin-top:18px;font-size:13px;font-weight:500;color:var(--gold)}
.view-all{position:absolute;left:524px;top:2227px;width:153px;height:42px;line-height:42px;font-size:15px}

/* calculator */
.calc{position:absolute;top:2356px;left:0;width:1200px;height:462px;background:linear-gradient(100deg,#2e4d6e 0%,#4f6d8c 45%,#7e95ad 75%,#3c5670 100%)}
.calc h2{position:absolute;left:122px;top:128px;color:#fff;font-size:30px;font-weight:700}
.calc .fee{position:absolute;left:98px;top:174px;color:var(--gold);font-size:23px;font-weight:700}
.calc .note{position:absolute;left:98px;width:520px;text-align:center;color:#fff;font-size:16px}
.calc .input{position:absolute;left:223px;top:305px;width:264px;height:42px;background:#fff;font-size:14px;color:#555;text-align:center;line-height:42px}

/* testimonials */
.testi{position:absolute;top:2982px;width:329px;height:216px;background:#fff;box-shadow:0 1px 6px rgba(0,0,0,.16);padding:40px 16px 0}
.quote{position:absolute;top:-26px;left:14px}
.testi p{font-size:13px;line-height:21px;color:var(--grey)}
.testi .who{display:flex;align-items:center;gap:16px;margin-top:16px}
.avatar{width:66px;height:66px;border-radius:50%;background:linear-gradient(135deg,#9aa3ad,#3c4450)}
.who b{font-size:16px;font-weight:500;display:block}
.stars{color:var(--gold);font-size:15px;letter-spacing:1px}

/* stores */
.store{position:absolute;top:3343px;width:176px;height:175px;border:2px solid var(--navy);display:flex;flex-direction:column;align-items:center;justify-content:center;font-size:24px;font-weight:700;color:var(--navy)}
.store.active{border-color:var(--gold)}
.store .btn{margin-top:14px;width:152px;height:36px;line-height:36px;font-size:16px;text-transform:none;font-weight:500}

/* footer */
.footer{position:absolute;top:3603px;left:0;width:1200px;height:320px;background:var(--navy-deep);color:#fff}
.footer .logo{position:absolute;left:87px;top:118px;width:218px;text-align:center}
.footer .logo .mark{width:36px;height:36px;border-radius:50%;background:#fff;margin:0 auto 10px}
.footer .logo .name{font-size:17px;font-weight:700}
.footer .logo .sub{font-size:9px;letter-spacing:4px;margin-top:4px}
.footer h5{position:absolute;top:30px;color:var(--gold);font-size:17px;font-weight:700}
.flinks{position:absolute;left:366px;top:68px;font-size:13px;font-weight:500;line-height:34px}
.fcontact{position:absolute;left:530px;top:66px;width:300px;font-size:13px;font-weight:500}
.fcontact .row{display:flex;gap:18px;margin-bottom:22px;line-height:19px}
.fcontact svg{flex:none}
.news{position:absolute;left:870px;top:57px;width:243px;height:43px;display:flex}
.news div{flex:1;background:#fff;color:#777;font-size:13px;line-height:43px;padding-left:10px}
.news span{width:43px;background:var(--gold);display:flex;align-items:center;justify-content:center}
.fsocial{position:absolute;left:870px;top:125px;display:flex;gap:12px}
.fsocial span{width:26px;height:26px;background:var(--gold);border-radius:3px}
.frule{position:absolute;left:87px;top:262px;width:1026px;height:1px;background:#3a4f6e}
.copy{position:absolute;top:286px;left:0;width:1200px;text-align:center;font-size:14px;font-weight:500}
</style>
</head>
<body>

<header class="topbar">
  <span class="welcome">Welcome To Our Website</span>
  <span class="login">Login / Register</span>
  <div class="social"><span></span><span></span><span></span><span></span></div>
</header>

<nav class="nav">
  <a class="active" style="left:223px">Home</a>
  <a style="left:305px">About</a>
  <a style="left:391px">Services</a>
  <div class="brand">
    <div class="mark"></div>
    <div class="name">MAR-WICK SKY HARBOR</div>
    <div class="sub">Custom Brokers Ltd</div>
  </div>
  <a style="left:748px">Reviews</a>
  <a style="left:846px">Blog</a>
  <a style="left:918px">Contact Us</a>
</nav>

<section class="hero" role="img" aria-label="Aerial view of a container ship sailing on dark sea water">
  <div class="hero-brand">
    <div class="name">MAR-WICK SKY HARBOR</div>
    <div class="sub">Custom Brokers Ltd.</div>
  </div>
  <a class="btn">Register Now</a>
  <div class="dots"><span></span><span class="on"></span><span></span></div>
</section>

<section class="strip">
  <div class="panel p1" role="img" aria-label="Warehouse workers handling boxes on a conveyor"></div>
  <div class="panel p2">
    <h3>Imports and Exports</h3>
    <p>It is a long established fact that a reader will be distracted by the readable content of a page when looking at its layout.</p>
    <a class="btn">Read More &raquo;</a>
  </div>
  <div class="panel p3" role="img" aria-label="Worker checking boxes in a warehouse aisle"></div>
  <span class="arrow-l">&lsaquo;</span><span class="arrow-r">&rsaquo;</span>
</section>

<div class="why-photo" role="img" aria-label="Logistics worker standing in front of a fleet of blue trucks"></div>
<section class="why-text">
  <h2>WHY CHOOSE US ?</h2>
  <p>It is a long established fact that a reader will be distracted by the readable content of a page when looking at its layout. It is a long established fact that a reader will be distracted by the readable content</p>
  <p>It is a long established fact that a reader will be distracted by the readable content of a page when looking at its layout.</p>
  <a class="read-more">Read More &raquo;</a>
</section>
<div class="why-icons">
  <span><svg width="34" height="26" viewBox="0 0 34 26"><path d="M2 8h7l8 6 8-6h7v10h-6l-9 6-9-6H2z" fill="#fff"/></svg></span>
  <span><svg width="26" height="30" viewBox="0 0 26 30"><path d="M6 13V8a7 7 0 0 1 14 0" stroke="#fff" stroke-width="3" fill="none"/><rect x="3" y="13" width="20" height="15" rx="2" fill="#fff"/></svg></span>
  <span><svg width="28" height="28" viewBox="0 0 28 28"><rect x="3" y="12" width="6" height="13" fill="#fff"/><path d="M11 12l5-9c3 0 3 3 2 7h6c2 0 3 2 2 4l-3 10H11z" fill="#fff"/></svg></span>
  <span><svg width="24" height="30" viewBox="0 0 24 30"><path d="M12 2a9 9 0 0 1 9 9c0 7-9 17-9 17S3 18 3 11a9 9 0 0 1 9-9z" fill="#fff"/><circle cx="12" cy="11" r="3.5" fill="var(--gold)"/></svg></span>
</div>

<section class="features">
  <div class="feature" style="left:153px"><div class="ring"><svg width="110" height="80" viewBox="0 0 110 80" fill="none" stroke="#fff" stroke-width="7" stroke-linecap="round"><path d="M8 12h50M18 28h30M28 44h18"/><circle cx="72" cy="44" r="28"/><path d="M72 28v17l10 9"/></svg></div><h4>FAST</h4></div>
  <div class="feature" style="left:392px"><div class="ring"><svg width="80" height="96" viewBox="0 0 80 96"><path d="M22 44V30a18 18 0 0 1 36 0v14" stroke="#fff" stroke-width="8" fill="none"/><rect x="14" y="42" width="54" height="46" rx="5" fill="#fff"/><circle cx="41" cy="62" r="6" fill="var(--navy)"/><rect x="38" y="62" width="6" height="14" fill="var(--navy)"/><path d="M2 56h12M0 66h14M2 76h12" stroke="#fff" stroke-width="6" stroke-linecap="round"/></svg></div><h4>SECURE</h4></div>
  <div class="feature" style="left:631px"><div class="ring"><svg width="104" height="80" viewBox="0 0 104 80" fill="none" stroke="#fff" stroke-width="6" stroke-linejoin="round"><path d="M8 30l64-22 18 40-64 22z"/><circle cx="50" cy="38" r="10"/><path d="M4 42l18 30 70-18"/></svg></div><h4>AFFORDABLE</h4></div>
  <div class="feature" style="left:870px"><div class="ring"><svg width="112" height="80" viewBox="0 0 112 80" fill="none" stroke="#fff" stroke-width="6" stroke-linejoin="round"><path d="M46 10h60v46H46zM46 28H24L8 46v14h38"/><path d="M58 48l40-30M72 48l26-18"/><circle cx="26" cy="64" r="9" fill="var(--navy)"/><circle cx="88" cy="64" r="9" fill="var(--navy)"/></svg></div><h4>COVENIENT</h4></div>
</section>

<h2 class="sec-title" style="top:1718px;color:var(--navy)">BLOG POST</h2>
<article class="post" style="left:87px">
  <div class="ph" role="img" aria-label="Cardboard boxes moving along rollers" style="background:linear-gradient(135deg,#b89a72,#6e6a66)"></div>
  <div class="body">
    <h3>It is a long established fact that a reader will be distracted</h3>
    <div class="meta"><span>&#9638; 18 March 2020</span><span>&#9679; By Admin</span></div>
    <p>It is a long established fact that a reader will be distracted by the readable content of a page when looking at its layout. The point of using Lorem Ipsum</p>
    <a class="more">READ MORE &raquo;</a>
  </div>
</article>
<article class="post featured" style="left:435px">
  <div class="ph" role="img" aria-label="Truck, ship and plane at a port at sunset" style="background:linear-gradient(180deg,#4a5f86,#d58a3a 60%,#3a3a48)"></div>
  <div class="body">
    <h3>It is a long established fact that a reader will be distracted</h3>
    <div class="meta"><span>&#9638; 18 March 2020</span><span>&#9679; By Admin</span></div>
    <p>It is a long established fact that a reader will be distracted by the readable content of a page when looking at its layout. The point of using Lorem Ipsum</p>
    <a class="more">READ MORE &raquo;</a>
  </div>
</article>
<article class="post" style="left:783px">
  <div class="ph" role="img" aria-label="Courier handing a parcel to a customer at the door" style="background:linear-gradient(135deg,#8a6a4c,#c8ad8e 60%,#6e5a48)"></div>
  <div class="body">
    <h3>It is a long established fact that a reader will be distracted</h3>
    <div class="meta"><span>&#9638; 18 March 2020</span><span>&#9679; By Admin</span></div>
    <p>It is a long established fact that a reader will be distracted by the readable content of a page when looking at its layout. The point of using Lorem Ipsum</p>
    <a class="more">READ MORE &raquo;</a>
  </div>
</article>
<a class="btn view-all">View All</a>

<section class="calc" role="img" aria-label="Cargo ship loaded with containers under a cloudy sky">
  <h2>SHIPPING WEIGHT CALCULATOR</h2>
  <div class="fee">Estimated freight cost/courier fee is: $: 0 USD.</div>
  <div class="note" style="top:202px;font-weight:700">(Based on weight of package only)</div>
  <div class="note" style="top:244px;font-size:15px;line-height:20px">Packages over $ 50.00 usd in value are subjected to Custom charges.<br>Please contact one of our offices for further details.</div>
  <div class="input">Packages Weight (lbs)</div>
</section>

<h2 class="sec-title" style="top:2897px;color:var(--gold)">WHAT CLIENTS SAY</h2>
<div class="testi" style="left:93px">
  <svg class="quote" width="58" height="50" viewBox="0 0 58 50"><path d="M2 2h24v26L14 48H4l8-20H2zM32 2h24v26L44 48H34l8-20H32z" fill="var(--gold)"/></svg>
  <p>It is a long established fact that a reader will be distracted by the readable content of a page when looking at its layout. The point of using Lorem Ipsum</p>
  <div class="who"><div class="avatar" role="img" aria-label="Client portrait"></div><div><b>Devon Clarke</b><span class="stars">&#9733;&#9733;&#9733;&#9733;&#9733;</span></div></div>
</div>
<div class="testi" style="left:438px">
  <svg class="quote" width="58" height="50" viewBox="0 0 58 50"><path d="M2 2h24v26L14 48H4l8-20H2zM32 2h24v26L44 48H34l8-20H32z" fill="var(--gold)"/></svg>
  <p>It is a long established fact that a reader will be distracted by the readable content of a page when looking at its layout. The point of using Lorem Ipsum</p>
  <div class="who"><div class="avatar" role="img" aria-label="Client portrait"></div><div><b>Marla Reid</b><span class="stars">&#9733;&#9733;&#9733;&#9733;&#9733;</span></div></div>
</div>
<div class="testi" style="left:783px">
  <svg class="quote" width="58" height="50" viewBox="0 0 58 50"><path d="M2 2h24v26L14 48H4l8-20H2zM32 2h24v26L44 48H34l8-20H32z" fill="var(--gold)"/></svg>
  <p>It is a long established fact that a reader will be distracted by the readable content of a page when looking at its layout. The point of using Lorem Ipsum</p>
  <div class="who"><div class="avatar" role="img" aria-label="Client portrait"></div><div><b>Andre Whyte</b><span class="stars">&#9733;&#9733;&#9733;&#9733;&#9733;</span></div></div>
</div>

<h2 class="sec-title" style="top:3278px;color:var(--gold)">ONLINE STORES</h2>
<div class="store" style="left:163px">Parcelora</div>
<div class="store" style="left:396px">Volt Mart</div>
<div class="store active" style="left:629px">Bidnest<a class="btn">Visit Website</a></div>
<div class="store" style="left:862px">Hometrove</div>

<footer class="footer">
  <div class="logo">
    <div class="mark"></div>
    <div class="name">MAR-WICK SKY HARBOR</div>
    <div class="sub">Custom Brokers Ltd.</div>
  </div>
  <h5 style="left:366px">QUICK LINKS</h5>
  <div class="flinks"><div>Home</div><div>About Us</div><div>Services</div><div>Reviews</div><div>Blog</div><div>Contact Us</div></div>
  <h5 style="left:531px">CONTACT US</h5>
  <div class="fcontact">
    <div class="row"><svg width="16" height="22" viewBox="0 0 24 30"><path d="M12 2a9 9 0 0 1 9 9c0 7-9 17-9 17S3 18 3 11a9 9 0 0 1 9-9z" fill="var(--gold)"/><circle cx="12" cy="11" r="3.5" fill="var(--navy-deep)"/></svg><span>Shop 9 Birchfield Trade Centre, 227-229 Welland Avenue Kingston 8, Jamaica West Indies</span></div>
    <div class="row"><svg width="20" height="20" viewBox="0 0 24 24"><path d="M5 2l4 1 2 5-3 2c1 3 3 5 6 6l2-3 5 2 1 4c-1 2-3 3-5 3C9 21 3 15 2 7c0-2 1-4 3-5z" fill="var(--gold)"/></svg><span>(876)555-0193</span></div>
    <div class="row"><svg width="20" height="16" viewBox="0 0 24 18"><rect x="1" y="1" width="22" height="16" fill="var(--gold)"/><path d="M1 1l11 9 11-9" stroke="var(--navy-deep)" stroke-width="2" fill="none"/></svg><span>info@marwickskyharbor-example.com</span></div>
  </div>
  <h5 style="left:870px">NEWSLETTER</h5>
  <div class="news"><div>Enter Email</div><span><svg width="22" height="22" viewBox="0 0 24 24" fill="none" stroke="#fff" stroke-width="3"><circle cx="10" cy="10" r="7"/><path d="M15 15l7 7"/></svg></span></div>
  <div class="fsocial"><span></span><span></span><span></span><span></span></div>
  <div class="frule"></div>
  <div class="copy">Copyrights &copy; Company Name 2020. All rights reserved.</div>
</footer>

</body>
</html>
```